Email Marketing Newsletter Design

Require the design of a email marketing newsletter. I will convert it into an updatable html template. I have supplied the copy for the first edition.

The newsletter is for a company that provides commercial property maintenance services such as office cleaning, lawns & gardens, electrical work etc

Web Site for client is:

http://morvelta.com.au/cgi-bin/xmlweb.cgi/home/index_html
Updates

Hi Wren

I will upload the doc as a PDF.

The width needs to be 777px

Look forward to seeing your design

Rgds
Derek

Target Market(s)

Property Facility Managers and Maintenance Managers working for commerical office buildings and large corporate sites

Industry/Entity Type

Construction

Number of Pages Required

1 page

Requirements
Must have
• Must be 777px wide
• Strong branding

• Intro paragraph

• Monthly Specials section

• Service Feature section

• Simple but clean with strong design elements
Nice to have
• Send to a friend icon

```html
<!DOCTYPE html>
<html lang="en">
<head>
<meta charset="utf-8">
<title>Morvelta Property Services Group – December 2009 E-Newsletter</title>
<link rel="stylesheet" href="https://fonts.googleapis.com/css2?family=Arimo:ital,wght@0,400;0,700;1,400;1,700&family=Open+Sans:wght@400;600&display=swap">
<style>
  :root {
    --navy: #063b7c;
    --navy-deep: #032d63;
    --green: #5a9a2c;
    --green-light: #8cc63f;
    --bar-blue: #cfe0f3;
    --bar-blue-light: #e4eef9;
    --text: #555555;
    --white: #ffffff;
  }
  * { box-sizing: border-box; margin: 0; padding: 0; }
  html, body {
    width: 935px; height: 1200px; overflow: hidden;
    background: var(--white);
  }
  .newsletter {
    position: relative;
    width: 777px; height: 997px;
    transform: scale(1.2033);
    transform-origin: 0 0;
    font-family: "Arimo", Arial, sans-serif;
    color: var(--text);
  }
  .masthead { position: absolute; left: 5px; top: 5px; width: 767px; height: 185px; }
  .masthead svg { position: absolute; inset: 0; }
  .brand-name {
    position: absolute; left: 100px; top: 28px;
    font-family: "Arimo", Arial, sans-serif; font-weight: 700;
    font-size: 60px; letter-spacing: 2px; color: var(--white); line-height: 1;
  }
  .brand-tagline {
    position: absolute; left: 167px; top: 86px;
    font-family: "Open Sans", Arial, sans-serif;
    font-size: 23px; color: var(--white); line-height: 1;
  }
  .issue-date {
    position: absolute; left: 432px; top: 136px;
    font-family: "Open Sans", Arial, sans-serif; font-weight: 600;
    font-size: 16px; color: var(--white);
  }
  .edition-badge {
    position: absolute; left: 587px; top: 22px;
    width: 112px; height: 112px;
  }
  .edition-badge span {
    position: absolute; left: 0; top: 30px; width: 112px;
    text-align: center; transform: rotate(-28deg);
    font-weight: 700; font-size: 16px; line-height: 17px; color: var(--navy);
  }
  .send-friend {
    position: absolute; left: 631px; top: 197px;
    display: flex; align-items: center; gap: 5px;
    font-size: 12px; font-weight: 700; color: var(--navy);
  }
  .section-bar {
    position: absolute; left: 5px; width: 767px; height: 32px;
    padding-left: 24px; display: flex; align-items: center;
    font-size: 18px; font-weight: 700; color: var(--navy);
    background: linear-gradient(100deg, var(--bar-blue) 0%, var(--bar-blue) 80%, var(--bar-blue-light) 88%, var(--bar-blue) 94%);
  }
  .section-bar--green {
    color: var(--white);
    background: linear-gradient(100deg, var(--green) 0%, var(--green) 80%, var(--green-light) 90%, var(--green) 96%);
  }
  .section-copy {
    position: absolute; font-size: 14px; line-height: 18px; color: var(--text);
  }
  .section-copy p + p { margin-top: 18px; }
  .highlight { color: var(--green); font-weight: 700; }
  .building-photo {
    position: absolute; left: 27px; top: 289px; width: 143px; height: 145px;
    padding: 2px; background: var(--white);
    box-shadow: 1px 1px 4px rgba(0,0,0,.35);
  }
  .building-photo div {
    width: 100%; height: 100%;
    background: linear-gradient(180deg, #2c5fa8 0%, #7fa6d4 45%, #dfe6ee 75%, #6a8d4a 100%);
  }
</style>
</head>
<body>
<main class="newsletter">

  <header class="masthead">
    <svg width="767" height="185" viewBox="0 0 767 185" aria-hidden="true">
      <path d="M0 0 H767 V95 C640 115 560 185 420 178 C280 172 150 130 0 122 Z" fill="var(--navy)"/>
      <path d="M767 92 V112 C680 125 600 185 430 180 C560 182 640 120 767 92 Z" fill="var(--green)"/>
      <path d="M767 100 C690 110 620 160 520 178 C630 168 700 120 767 108 Z" fill="var(--green-light)" opacity=".6"/>
    </svg>
    <div class="brand-name">MORVELTA</div>
    <div class="brand-tagline">Property Services Group</div>
    <div class="edition-badge">
      <svg width="112" height="112" viewBox="0 0 112 112" aria-hidden="true">
        <polygon fill="var(--green-light)" stroke="#b9df7c" stroke-width="1.5"
          points="56,2 64,18 79,8 81,26 99,22 94,40 110,46 97,58 108,72 90,75 93,93 76,88 70,106 56,95 42,106 36,88 19,93 22,75 4,72 15,58 2,46 18,40 13,22 31,26 33,8 48,18"/>
      </svg>
      <span>1st<br>EDITION</span>
    </div>
    <div class="issue-date">December 2009&nbsp; E-Newsletter</div>
  </header>

  <a class="send-friend">
    <svg width="20" height="12" viewBox="0 0 20 12" aria-hidden="true">
      <rect x="0.5" y="0.5" width="19" height="11" fill="var(--navy)" stroke="var(--navy-deep)"/>
      <path d="M1 1 L10 7 L19 1" fill="none" stroke="var(--white)" stroke-width="1"/>
    </svg>
    Send to a Friend
  </a>

  <h2 class="section-bar" style="top:234px">Welcome</h2>
  <figure class="building-photo"><div role="img" aria-label="Photo of a modern curved glass office building against a blue sky"></div></figure>
  <div class="section-copy" style="left:190px; top:312px; width:560px;">
    <p><i>Morvelta</i> is pleased to present our <span class="highlight">first e-newsletter</span>. We believe in making life easier for our clients. So, we have created an e-newsletter to let you know about our current promotions and the services that we offer.</p>
    <p>Please enjoy learning about the range of ways <i>Morvelta</i> can look after your office cleaning and maintenance needs.</p>
  </div>

  <h2 class="section-bar" style="top:477px">December Offer: FREE Expert Morvelta Carpet and Window Clean</h2>
  <div class="section-copy" style="left:27px; top:530px; width:725px;">
    <p>At <i>Morvelta</i>, we believe in rewarding our loyal customers. This month, we are offering a <span class="highlight">FREE</span> carpet and window clean if you engage our standard office cleaning services for at least 6 months.</p>
    <p><span class="highlight">There are no strings attached and nocontracts to sign!</span><br>Call <i>Morvelta</i> today and allow us to manage all of your cleaning needs for you!</p>
  </div>

  <h2 class="section-bar section-bar--green" style="top:652px">Spotlight:&nbsp;<i>Morvelta</i>&nbsp;Cleaning Services</h2>
  <div class="section-copy" style="left:27px; top:705px; width:725px;">
    <p>A <i>Morvelta</i> office clean will look after all aspects of your office site. Our service includes regularly and thoroughly cleaning: floors, desks, kitchens and bathrooms. We also look after: window cleaning, carpet cleaning, vinyl floor stripping sealing, Venetian blind cleaning, floor sweeping, floor scrubbing, high pressure cleaning, ceiling tile and light cleaning and graffiti removal.</p>
    <p>We realise that cleaning should be a background activity. You won’t notice we are there; you will notice that you don’t need to self manage the cleaning process, we do that for you.</p>
    <p>Allow our experienced, expert staff to project manage all of your regular, and irregular, office cleaning needs!</p>
  </div>

</main>
</body>
</html>
```